Leading Nutrition Company Needs a Stylish Label Design!

We need a label/packaging design for our new cutting-edge detox called "Clear Tide". It is an all organic detox that removes toxins, harsh-chemicals, herbicides, pesticides and heavy metals from the body. It essentially turns everything you eat into organic whole foods and without all the chemicals in our bodies, we run at optimal performance.

We are attempting to blend a modern, simplistic design for our label.
We would like to see designs that use flat grays, silvers and blacks. We would also like to see pops of green and or blue in the design. Overall design will be a modern, contemporary matte finish with pops of color in either a pattern design or colored lettering. The final design should convey a high-end, exclusive health product.

Target Market(s)

Health conscious individuals and those seeking to pass an upcoming drug test. Athletes, nutritionist, dietitians ranging from 18-70 years of age.

Industry/Entity Type

Health

Font styles to use
Other font styles liked:
• Unique modern fonts

Colors
b1b1b1
9d9d9d
474747
33a6d7
0192cd
9ccb3b

Requirements
Must have
• Must be modern and simplistic

Pops of color - Don't need to be matte

Matte finishes for background
-Light grays, graphite, light silvers etc

Lettering must be modern and unique

Label type wil be a "shrink label" for an 8 oz boston squat bottle
-See attached link for bottle

"Clear Tide" some where on label

Company logo some where on label
-See attached files for logo
Nice to have
• Cool background designs that provide depth to the design.

A strip of pattern design running vertically or horizontally to capture the eye.
-See attached pictures for examples
Should not have
• Script or Normal fonts

```html
<!DOCTYPE html>
<html lang="en">
<head>
<meta charset="utf-8">
<title>Clear Tide — Shrink Label</title>
<link href="https://fonts.googleapis.com/css2?family=Montserrat:wght@500;600&family=Space+Mono&display=swap" rel="stylesheet">
<style>
  :root {
    --canvas: #ffffff;
    --graphite: #2b2b2c;
    --graphite-deep: #1f1f20;
    --shield: #3a3a3c;
    --lime: #9ccb3b;
    --lime-light: #a9d44a;
    --green-deep: #23994a;
    --ink: #2a2a2a;
    --panel: rgba(235, 240, 228, 0.9);
    --white: #ffffff;
  }
  * { margin: 0; padding: 0; box-sizing: border-box; }
  html, body { width: 1200px; height: 724px; overflow: hidden; background: var(--canvas); }
  .canvas { position: relative; width: 1200px; height: 724px; }

  .label {
    position: absolute; left: 66px; top: 77px; width: 1052px; height: 432px;
    overflow: hidden;
    background: linear-gradient(180deg, var(--lime-light) 0%, var(--lime) 70%, var(--green-deep) 100%);
  }
  .label__band {
    position: absolute; left: 0; top: 0; width: 100%; height: 104px;
    background: linear-gradient(180deg, var(--graphite-deep), var(--graphite));
  }
  .label__texture {
    position: absolute; left: 0; top: 104px; width: 100%; height: 120px;
    background: linear-gradient(180deg, rgba(60, 110, 20, 0.25), rgba(60, 110, 20, 0));
  }
  .label__shield { position: absolute; left: 0; top: 0; }

  .brand {
    position: absolute; display: flex; align-items: center; gap: 6px;
    font-family: "Montserrat", sans-serif; font-weight: 600; color: var(--lime);
    font-size: 11px; letter-spacing: 0.5px;
  }
  .brand__dot { width: 12px; height: 12px; border-radius: 50%; background: var(--lime); }
  .brand--front { left: 272px; top: 88px; }
  .brand--back { left: 900px; top: 74px; }

  .title {
    position: absolute; left: 146px; top: 146px;
    font-family: "Montserrat", sans-serif; font-weight: 600; color: var(--lime);
    font-size: 84px; line-height: 78px; letter-spacing: 1px;
  }
  .volume {
    position: absolute; font-family: "Montserrat", sans-serif; font-weight: 600; color: var(--ink);
  }
  .volume small { font-size: 0.7em; font-weight: 500; }
  .volume--front { left: 244px; top: 397px; font-size: 16px; }

  .info-panel {
    position: absolute; left: 652px; top: 123px; width: 398px; height: 272px;
    background: var(--panel); border-radius: 10px;
  }
  .serving-note {
    position: absolute; left: 858px; top: 143px;
    font-family: "Space Mono", monospace; font-size: 8.5px; color: var(--ink);
  }
  .product {
    position: absolute; left: 667px; top: 152px; width: 170px;
    font-family: "Space Mono", monospace; color: var(--ink);
  }
  .product__name {
    font-family: "Montserrat", sans-serif; font-weight: 600; font-size: 21px; margin-bottom: 6px; letter-spacing: 0.5px;
  }
  .product__desc { font-size: 8.2px; line-height: 10.2px; text-align: justify; }
  .product__contact { margin-top: 12px; font-size: 8.2px; line-height: 10px; }

  .facts {
    position: absolute; left: 850px; top: 160px; width: 185px; height: 232px;
    border: 2px solid var(--graphite-deep); border-radius: 6px; background: var(--white);
    padding: 4px 8px; font-family: "Space Mono", monospace; color: var(--ink);
  }
  .facts__title {
    font-family: "Montserrat", sans-serif; font-weight: 600; font-size: 16px;
    border-bottom: 4px solid var(--graphite-deep); padding-bottom: 3px;
  }
  .facts__intake { font-size: 9px; padding: 3px 0 2px; border-bottom: 3px solid var(--graphite-deep); margin-bottom: 4px; }
  .facts__row { display: flex; justify-content: space-between; font-size: 8.6px; line-height: 10.1px; }

  .footer-name {
    position: absolute; left: 890px; top: 398px;
    font-family: "Montserrat", sans-serif; font-weight: 600; font-size: 13px; color: var(--ink);
  }
  .volume--back { left: 970px; top: 399px; font-size: 12px; }
</style>
</head>
<body>
<div class="canvas">
  <div class="label">
    <div class="label__band" role="img" aria-label="Dark graphite band with a perforated dot pattern"></div>
    <div class="label__texture" role="img" aria-label="Soft green dot pattern fading into the label"></div>

    <svg class="label__shield" width="540" height="380" viewBox="0 0 540 380" role="img" aria-label="Graphite shield shape with perforated dot pattern">
      <path d="M14 0 L522 0 L522 20 C515 200 400 330 174 372 C95 300 30 180 14 0 Z" fill="var(--shield)"/>
    </svg>

    <div class="brand brand--front"><span class="brand__dot"></span>Verdant Labs</div>
    <div class="brand brand--back"><span class="brand__dot"></span>Verdant Labs</div>

    <h1 class="title">CLEAR<br>TIDE</h1>
    <div class="volume volume--front">8.0<small>oz</small></div>

    <div class="info-panel"></div>
    <p class="serving-note">Best consumed chilled with 3-5 days</p>

    <div class="product">
      <h2 class="product__name">CLEAR TIDE</h2>
      <p class="product__desc">is an all organic detox that removes toxins, harsh-chemicals, herbicides, pesticides and heavy metals from the body. It essentially turns everything you eat into organic whole foods and without all the chemicals in our bodies, so you can function at optimal performance.</p>
      <p class="product__contact">Clear Tide<br>Address<br>Phone<br>Website</p>
    </div>

    <div class="facts">
      <div class="facts__title">Supplement Facts</div>
      <div class="facts__intake">DAILY INTAKE 3%</div>
      <div class="facts__row"><span>NUTRITIONAL FACTS</span><span>2.0 mg</span></div>
      <div class="facts__row"><span>NUTRITIONAL FACTS</span><span>2.0 mg</span></div>
      <div class="facts__row"><span>NUTRITIONAL FACTS</span><span>2.0 mg</span></div>
      <div class="facts__row"><span>NUTRITIONAL FACTS</span><span>2.0 mg</span></div>
      <div class="facts__row"><span>NUTRITIONAL FACTS</span><span>2.0 mg</span></div>
      <div class="facts__row"><span>NUTRITIONAL FACTS</span><span>2.0 mg</span></div>
      <div class="facts__row"><span>NUTRITIONAL FACTS</span><span>2.0 mg</span></div>
      <div class="facts__row"><span>NUTRITIONAL FACTS</span><span>2.0 mg</span></div>
      <div class="facts__row"><span>NUTRITIONAL FACTS</span><span>2.0 mg</span></div>
      <div class="facts__row"><span>NUTRITIONAL FACTS</span><span>2.0 mg</span></div>
      <div class="facts__row"><span>NUTRITIONAL FACTS</span><span>2.0 mg</span></div>
      <div class="facts__row"><span>NUTRITIONAL FACTS</span><span>2.0 mg</span></div>
      <div class="facts__row"><span>NUTRITIONAL FACTS</span><span>2.0 mg</span></div>
      <div class="facts__row"><span>NUTRITIONAL FACTS</span><span>2.0 mg</span></div>
      <div class="facts__row"><span>NUTRITIONAL FACTS</span><span>2.0 mg</span></div>
      <div class="facts__row"><span>NUTRITIONAL FACTS</span><span>2.0 mg</span></div>
    </div>

    <div class="footer-name">CLEAR TIDE</div>
    <div class="volume volume--back">8.0<small>oz</small></div>
  </div>
</div>
</body>
</html>
```